Design a Logo for Wine Label

Hello,
We're looking for a new wine label design for our 2015 vintage. We would like a cross section of both traditional and modern styles.
The name is Merrindee Creek Shiraz, feel free to incorporate that into the design if you will.
It would be preferable to be a Front and Back Label. Front would have the design element and the back label should have space for ingredients and other mandated health information.
A quick search would come up with results. I have intentionally not uploaded an existing label as I want a fresh look.
Thank you

```html
<!DOCTYPE html>
<html lang="en">
<head>
<meta charset="utf-8">
<title>Merrindee Creek Shiraz – Front Label</title>
<link rel="stylesheet" href="https://fonts.googleapis.com/css2?family=Cinzel:wght@600;700&family=Cormorant+Garamond:wght@600;700&display=swap">
<style>
  :root {
    --backdrop: #ecebea;
    --label-cream: #f4f0dc;
    --label-edge: #e4dec4;
    --wine-red: #8c1a2e;
    --vintage-olive: #877f45;
    --leaf-green: #8e9548;
    --grape-red: #9a1f36;
    --disc-tan: #ddd3a6;
  }
  * { margin: 0; padding: 0; box-sizing: border-box; }
  html, body {
    width: 1200px;
    height: 1200px;
    overflow: hidden;
    background: var(--backdrop);
  }
  .canvas {
    width: 1200px;
    height: 1200px;
    display: flex;
    align-items: center;
    justify-content: center;
  }
  .front-label {
    position: relative;
    width: 660px;
    height: 1080px;
    background: var(--label-cream);
    border: 1px solid var(--label-edge);
    display: flex;
    flex-direction: column;
    align-items: center;
  }
  .vintage {
    margin-top: 56px;
    display: flex;
    align-items: center;
    gap: 20px;
    color: var(--vintage-olive);
    font-family: "Cormorant Garamond", Georgia, serif;
    font-weight: 700;
    font-size: 38px;
    font-variant-numeric: lining-nums;
    letter-spacing: 0.3em;
  }
  .vintage-rule {
    display: block;
    width: 80px;
    height: 2px;
    background: var(--vintage-olive);
  }
  .vine-emblem {
    margin-top: 28px;
    width: 390px;
    height: 380px;
    border-radius: 24px;
    background: linear-gradient(180deg, var(--leaf-green) 0%, var(--disc-tan) 50%, var(--grape-red) 100%);
    opacity: 0.85;
  }
  .wine-name {
    margin-top: 86px;
    color: var(--wine-red);
    font-family: "Cinzel", "Times New Roman", serif;
    font-weight: 700;
    font-size: 58px;
    line-height: 86px;
    letter-spacing: 0.1em;
    text-align: center;
  }
  .wine-name span { display: block; }
  .volume {
    position: absolute;
    bottom: 44px;
    left: 0;
    right: 0;
    text-align: center;
    color: var(--vintage-olive);
    font-family: "Cormorant Garamond", Georgia, serif;
    font-weight: 700;
    font-size: 28px;
    font-variant-numeric: lining-nums;
  }
</style>
</head>
<body>
  <main class="canvas">
    <section class="front-label">
      <div class="vintage">
        <span class="vintage-rule"></span>
        <span class="vintage-year">2015</span>
        <span class="vintage-rule"></span>
      </div>
      <div class="vine-emblem" role="img" aria-label="Illustration of a vine leaf above a cluster of red grapes"></div>
      <h1 class="wine-name">
        <span>MERRINDEE</span>
        <span>CREEK</span>
        <span>SHIRAZ</span>
      </h1>
      <p class="volume">750ml</p>
    </section>
  </main>
</body>
</html>
```